Bref créative
Newspaper Ad for Immigration Law Firm
Need Three Ads/Sizes
I need a total of 3 newspaper ads with 3 different sizes.
1. Main Ad - 5 in x 2 in
2. 3.25 in x 2 in
3. 1.5 in x 2 in
Designers should submit their design based on the 5 in x 2 in. Once I have determined the "winning designer," I will work with that designer to create the other two ads using the same winning design.
Law
The following must be included: I will also upload my picture, my logo, and Board Certified Logo. Thanks.
1. Picture of Attorney
2. Attorney
3. Brian K. Wendell
4. Law Firm logo
5. Board Certified Logo
6. Immigration Law below Board Certified Logo
7. 4180 Millbrook Lane
8. Suite 318
9. Houston, Texas 77043
10. www.thewendellcounsel.com
11. Telephone: (713) 548-2190
12. Fax: (713) 548-2197
13. bkellan4471@mailvexo.com
14. Immigration Bonds
15. Deportation Cases
16. Immigration Court
17. Immigration Waivers
18. Immigration Appeals
19. Family Petitions
20. Citizenship
21. Permanent Residency
22. Asylum, TPS, NACARA
23. Work Permits
24. Other Immigration Cases
Law Firm Logo Should go on the very top i think
You can cut out background if you like. Or not, up to your design.
The phrase "Immigration Law" must be directly underneath this logo. Logo cannot be changed or altered.
Sample proof

```html
<!DOCTYPE html>
<html lang="en">
<head>
<meta charset="utf-8">
<title>Brian K. Wendell – Immigration Law Firm Newspaper Ad</title>
<link rel="stylesheet" href="https://fonts.googleapis.com/css2?family=Cinzel:wght@400;600&family=Crimson+Text:wght@400;600&display=swap">
<style>
  :root {
    --stage: #1c1c1c;
    --paper: #ffffff;
    --ink: #1a1a1a;
    --navy: #1f2a4a;
    --maroon-dark: #2a1512;
    --maroon: #5a2a22;
    --maroon-mid: #74392d;
    --photo-dark: #2b1a14;
    --photo-light: #7b5a45;
    --badge: #1f3f7a;
    --light: #f4efe9;
  }
  * { box-sizing: border-box; margin: 0; padding: 0; }
  html, body { width: 1200px; height: 901px; overflow: hidden; background: var(--stage); }
  .ad {
    position: absolute; left: 50px; top: 230px;
    width: 1100px; height: 440px;
    background: var(--paper); overflow: hidden;
    font-family: "Cinzel", serif; color: var(--ink);
  }
  /* Masthead / firm name */
  .firm { position: absolute; left: 22px; top: 22px; display: flex; align-items: center; gap: 18px; }
  .firm-mark { width: 104px; height: 104px; border-radius: 50%; background: var(--navy); flex: none; }
  .firm-name { font-family: "Cinzel", serif; font-weight: 600; color: var(--navy); text-align: center; line-height: 1.1; white-space: nowrap; }
  .firm-name .pre { font-size: 24px; display: block; }
  .firm-name .name { font-size: 40px; display: block; letter-spacing: .5px; }
  .firm-name .post { font-size: 24px; display: block; letter-spacing: 1px; }

  /* Certification */
  .cert { position: absolute; left: 588px; top: 60px; width: 160px; }
  .cert-badge { width: 160px; height: 46px; background: var(--badge); }
  .cert-label { font-family: "Crimson Text", serif; font-size: 15px; color: var(--ink); margin-top: 4px; }

  /* Practice areas band */
  .services {
    position: absolute; left: 0; top: 154px; width: 760px; height: 204px;
    background: linear-gradient(90deg, var(--maroon-dark), var(--maroon) 55%, var(--maroon-mid));
    display: grid; grid-template-columns: 236px 258px 1fr; padding: 20px 0 0 22px;
  }
  .services ul { list-style: none; }
  .services li {
    color: var(--light); font-size: 17px; line-height: 1.1; margin-bottom: 25px;
    padding-left: 15px; position: relative; letter-spacing: .3px; white-space: nowrap;
  }
  .services li::before {
    content: ""; position: absolute; left: 0; top: 6px; width: 6px; height: 6px; background: var(--light);
  }
  .services li.wrap { margin-bottom: 10px; }

  /* Contact strip */
  .contact { position: absolute; left: 0; top: 358px; width: 760px; height: 82px; padding: 10px 20px; }
  .address { font-family: "Crimson Text", serif; font-size: 16px; line-height: 1.2; color: var(--ink); }
  .web { font-family: "Crimson Text", serif; font-size: 15px; letter-spacing: 3px; margin-top: 2px; }
  .phone {
    position: absolute; right: 66px; top: 12px;
    font-family: "Crimson Text", serif; font-size: 54px; font-weight: 600; color: var(--ink); line-height: 1;
  }

  /* Attorney portrait */
  .portrait {
    position: absolute; left: 760px; top: 0; width: 340px; height: 440px;
    background: radial-gradient(ellipse at 60% 45%, var(--photo-light), var(--photo-dark) 75%);
  }
  .attorney { position: absolute; right: 22px; top: 22px; text-align: right; color: var(--light); }
  .attorney .who { font-size: 17px; }
  .attorney .role { font-size: 11px; letter-spacing: 1px; }
</style>
</head>
<body>
  <section class="ad">
    <header class="firm">
      <div class="firm-mark"></div>
      <div class="firm-name">
        <span class="pre">Law Office of</span>
        <span class="name">BRIAN K. WENDELL</span>
        <span class="post">Immigration Law Firm</span>
      </div>
    </header>

    <div class="cert">
      <div class="cert-badge" role="img" aria-label="Board certification badge"></div>
      <div class="cert-label">Immigration Law</div>
    </div>

    <div class="services">
      <ul>
        <li>Immigration Bonds</li>
        <li>Deportation Cases</li>
        <li>Immigration Court</li>
        <li>Immigration Waivers</li>
      </ul>
      <ul>
        <li>Immigration Appeals</li>
        <li>Family Petitions</li>
        <li>Citizenship</li>
        <li>Permanent Residency</li>
      </ul>
      <ul>
        <li class="wrap">Asylum, TPS,<br>NACARA</li>
        <li class="wrap">Work Permits</li>
        <li>Other<br>Immigration<br>Cases</li>
      </ul>
    </div>

    <footer class="contact">
      <p class="address">4180 Millbrook Lane Suite 318 Houston, Texas 77043</p>
      <p class="address">Fax: (713) 548-2197 &nbsp; Email: bkellan4471@mailvexo.com</p>
      <p class="web">www.thewendellcounsel.com</p>
      <p class="phone">(713) 548-2190</p>
    </footer>

    <div class="portrait" role="img" aria-label="Portrait photo of the attorney in a dark suit, seated in a leather chair">
      <div class="attorney">
        <div class="who">Brian K. Wendell</div>
        <div class="role">ATTORNEY</div>
      </div>
    </div>
  </section>
</body>
</html>
```